Minimalist Professional Business Card Design

We will be revamping our marketing materials: Business cards, Website and Catalogs.
Our Overall Design direction is to have a Minimalist artwork with Professionalism and Premium feel. The revamp starts with the new business card design followed by the others. Thus the designer whom work is selected for this job will likely to follow through with the subsequent jobs.

Target Market(s)

Upscale

Industry/Entity Type

Manufacturing

Contact Information for Business Card

For the Business Cards, the following are required:
. Minimalist yet Professional and Premium Feel
. Background Colors: white and / or light pastel yellow and if needed to smoothen the yellow, the light grey can be incorporated. We are changing our corporate bright yellow to either one of the three alternatives:
1. Soylant yellow CMYK (1%, 0%, 52%, 3%)
2. Popcorn yellow CMYK (0%, 0%, 33%, 0%)
3. Papaya yellow CMYK (0%, 0%, 51%, 0%)

Information to be inputed in the business cards:

Name: Barlen Moritova
Position: Managing Director

Company's name: Vellomar Valves Pte. Ltd.
Address: 512 Halvick Lane #07-09B
Singapore 617302
Tel: (65) 6281 4096
Fax: (65) 6294 7118
Email: barlen@vellomarvalves-example.com
Website: www.vellomarvalves-example.com
Skype: Vellomar.Valves
Chatwell/ Linko/ Vibra/ TalkNow: (65) 9372 6081

Company's Logo
Company's Slogan
Two product photos placed side by side (if this gets into the way of the design, it is OK not to include them)

Font styles to use
Serif

Colors
ffffff

Requirements
Must have
• Minimalist
Should not have
• Messy, crowded, playful

```html
<!DOCTYPE html>
<html lang="en">
<head>
<meta charset="utf-8">
<title>Vellomar Valves – Business Card</title>
<link href="https://fonts.googleapis.com/css2?family=Alegreya+SC:wght@400;500&display=swap" rel="stylesheet">
<style>
  :root {
    --backdrop: #474744;
    --card: #ebe8b2;
    --ink: #4a4a46;
    --ink-soft: #5a5a54;
    --mark-faint: #d9d59f;
  }
  * { margin: 0; padding: 0; box-sizing: border-box; }
  html, body {
    width: 1200px; height: 1200px; overflow: hidden;
    background: var(--backdrop);
    font-family: "Alegreya SC", Georgia, serif;
    color: var(--ink);
  }
  .card {
    position: absolute;
    width: 660px; height: 377px;
    background: var(--card);
    overflow: hidden;
  }
  .card--front { left: 80px; top: 130px; }
  .card--back { left: 460px; top: 650px; }

  /* Front */
  .brand {
    position: absolute; left: 0; right: 0; top: 120px;
    display: flex; align-items: center; justify-content: center; gap: 18px;
  }
  .brand__dot {
    width: 58px; height: 58px; border-radius: 50%;
    border: 9px solid var(--ink);
  }
  .brand__name {
    font-size: 50px; font-weight: 500; letter-spacing: 3px; line-height: 1;
  }
  .slogan {
    position: absolute; left: 0; right: 0; top: 236px;
    text-align: center; font-size: 21px; letter-spacing: 2.5px;
  }

  /* Back */
  .faint-mark {
    position: absolute; left: 10px; top: 60px;
    width: 330px; height: 330px; border-radius: 50%;
    background: var(--mark-faint);
  }
  .person { position: absolute; left: 300px; top: 40px; }
  .person__name { font-size: 30px; font-weight: 500; letter-spacing: 2px; line-height: 1; }
  .person__role { font-size: 13px; letter-spacing: 5px; margin-top: 4px; color: var(--ink-soft); }
  .contacts {
    position: absolute; left: 300px; top: 118px;
    list-style: none; font-size: 14px; letter-spacing: 0.5px;
  }
  .contacts li { display: flex; align-items: center; gap: 9px; height: 27px; }
  .contacts svg { width: 20px; height: 20px; flex: none; }
  .chat {
    position: absolute; left: 300px; right: 30px; top: 296px;
    text-align: right; font-size: 14px; letter-spacing: 0.5px;
  }
  .company {
    position: absolute; left: 200px; top: 340px;
    font-size: 13px; letter-spacing: 0.8px; color: var(--ink-soft);
  }
</style>
</head>
<body>

<section class="card card--front">
  <div class="brand">
    <span class="brand__dot"></span>
    <span class="brand__name">VELLOMAR</span>
  </div>
  <p class="slogan">Made With Pride | For Heavy Duty</p>
</section>

<section class="card card--back">
  <div class="faint-mark" role="img" aria-label="Faint company mark"></div>

  <div class="person">
    <p class="person__name">Barlen Moritova</p>
    <p class="person__role">Managing Director</p>
  </div>

  <ul class="contacts">
    <li>
      <svg viewBox="0 0 20 20"><circle cx="10" cy="10" r="9" fill="none" stroke="#4a4a46" stroke-width="1.4"/><path d="M10 15s-3.5-3.6-3.5-6a3.5 3.5 0 0 1 7 0c0 2.4-3.5 6-3.5 6z" fill="#4a4a46"/><circle cx="10" cy="9" r="1.2" fill="#ebe8b2"/></svg>
      512 Halvick Lane #07-09B, Singapore 617302
    </li>
    <li>
      <svg viewBox="0 0 20 20"><circle cx="10" cy="10" r="9" fill="none" stroke="#4a4a46" stroke-width="1.4"/><path d="M7 5.5l1.8 2.2-1 1.2c.7 1.4 1.7 2.4 3.1 3.1l1.2-1 2.2 1.8-.9 1.7c-3.6-.4-6.9-3.7-7.3-7.3z" fill="#4a4a46"/></svg>
      (65) 6281 4096
    </li>
    <li>
      <svg viewBox="0 0 20 20"><circle cx="10" cy="10" r="9" fill="#4a4a46"/><rect x="6" y="7.5" width="8" height="6" rx="1" fill="#ebe8b2"/><rect x="7.5" y="5" width="5" height="3" fill="#ebe8b2"/></svg>
      (65) 6294 7118
    </li>
    <li>
      <svg viewBox="0 0 20 20"><circle cx="10" cy="10" r="9" fill="#4a4a46"/><rect x="5.5" y="6.5" width="9" height="7" fill="#ebe8b2"/><path d="M5.5 6.5l4.5 4 4.5-4" fill="none" stroke="#4a4a46" stroke-width="1"/></svg>
      barlen@vellomarvalves-example.com
    </li>
    <li>
      <svg viewBox="0 0 20 20"><circle cx="10" cy="10" r="9" fill="#4a4a46"/><circle cx="10" cy="10" r="5" fill="none" stroke="#ebe8b2" stroke-width="1.2"/><path d="M5 10h10M10 5c-2.5 3-2.5 7 0 10M10 5c2.5 3 2.5 7 0 10" fill="none" stroke="#ebe8b2" stroke-width="1"/></svg>
      www.vellomarvalves-example.com
    </li>
    <li>
      <svg viewBox="0 0 20 20"><circle cx="10" cy="10" r="9" fill="none" stroke="#4a4a46" stroke-width="1.4"/><circle cx="10" cy="10" r="5" fill="#4a4a46"/></svg>
      Vellomar.Valves
    </li>
  </ul>

  <p class="chat">Chatwell/ Linko/ Vibra/ TalkNow: (65) 9372 6081</p>

  <p class="company">Vellomar Valves Pte. Ltd.</p>
</section>

</body>
</html>
```